Stationery Design Project - Technica-Prime

Business Cards
Size: 90mm x 55mm

Letterhead
Size: A4 - 210mm x 297mm

With Compliments Slip
Size: DL - 210mm x 99mm

Notepad
Size: 250mm x 140mm

Presentation Folder
Size: A4

Technica-Prime
*Perth *Brisbane *Seoul *Hongkong

website: www.technicaprime-example.com.au (Currently live, but being replaced with new one)

Engineering and Technical recruitment company for the Mining, Oil & Gas, Construction & Engineering Sectors

Industry/Entity Type

Business

```html
<!DOCTYPE html>
<html lang="en">
<head>
<meta charset="utf-8">
<title>Technica-Prime Business Card Set</title>
<link rel="stylesheet" href="https://fonts.googleapis.com/css2?family=Didact+Gothic&display=swap">
<style>
  :root {
    --backdrop: #6e4a30;
    --card: #ffffff;
    --ink: #333333;
    --ink-soft: #555555;
    --brand-blue: #2b8ab8;
    --swoosh-grey: #8a8d91;
    --label: #1e1610;
    --faint-mark: #eceef1;
  }
  * { margin: 0; padding: 0; box-sizing: border-box; }
  html, body { width: 1200px; height: 788px; overflow: hidden; }
  body {
    background: var(--backdrop);
    font-family: "Didact Gothic", sans-serif;
    color: var(--ink);
    position: relative;
  }
  .view-label {
    position: absolute;
    width: 525px;
    text-align: center;
    font-size: 22px;
    color: var(--label);
  }
  .card {
    position: absolute;
    width: 525px;
    height: 300px;
    background: var(--card);
    border-radius: 22px;
    overflow: hidden;
  }
  .card svg.art { position: absolute; left: 0; top: 0; }
  .brand { position: absolute; display: flex; align-items: center; }
  .brand-dot { border-radius: 50%; background: var(--brand-blue); flex: none; }
  .brand-name { color: var(--ink-soft); letter-spacing: 1px; white-space: nowrap; }
  .cities {
    position: absolute; left: 0; width: 100%;
    text-align: center; font-size: 18px; color: var(--ink);
  }

  /* front */
  .contact { position: absolute; left: 44px; top: 132px; }
  .contact-name { font-size: 17px; color: var(--brand-blue); margin-bottom: 6px; }
  .contact-name small { font-size: 13.5px; }
  .contact-line { font-size: 13.5px; line-height: 24px; }
  .contact-line b { font-weight: 700; }
  .address {
    position: absolute; right: 18px; top: 246px;
    text-align: right; color: #fff; font-size: 13.5px; line-height: 19px;
  }

  /* back 3 */
  .photo-strip { position: absolute; left: 0; top: 115px; width: 525px; height: 93px; display: flex; }
  .photo { flex: 1; }
  .photo.reclaimer { background: linear-gradient(180deg, #6d9bc9 0%, #a98660 70%, #8b4f2c 100%); }
  .photo.turbine { background: linear-gradient(180deg, #9db5cc 0%, #d9e1e8 55%, #3d5e80 100%); }
  .photo.platform { background: linear-gradient(180deg, #27466b 0%, #2f4f74 60%, #1d3352 100%); }
  .photo.carrier { background: linear-gradient(180deg, #6d8aa8 0%, #cfd4d6 50%, #2a4a68 100%); }
</style>
</head>
<body>

  <div class="view-label" style="left:54px; top:32px;">Front</div>
  <div class="view-label" style="left:622px; top:32px;">Back - 1</div>
  <div class="view-label" style="left:54px; top:402px;">Back - 2</div>
  <div class="view-label" style="left:622px; top:402px;">Back - 3</div>

  <!-- Front -->
  <section class="card card-front" style="left:54px; top:74px;">
    <svg class="art" width="525" height="300" viewBox="0 0 525 300" aria-hidden="true">
      <path d="M0,262 C200,286 400,228 525,112 L525,142 C400,246 200,282 0,266 Z" fill="var(--swoosh-grey)"/>
      <path d="M0,272 C200,292 400,252 525,158 L525,300 L0,300 Z" fill="var(--brand-blue)"/>
    </svg>
    <div class="brand" style="left:46px; top:34px;">
      <span class="brand-dot" style="width:72px; height:72px;"></span>
      <span class="brand-name" style="font-size:34px; margin-left:22px;">technicaprime</span>
    </div>
    <div class="contact">
      <p class="contact-name">Your Name, <small>Designation</small></p>
      <p class="contact-line"><b>cell</b> : +12 345 67 8910</p>
      <p class="contact-line"><b>phone</b> : +12 345 67 8910</p>
      <p class="contact-line"><b>email</b> : info@yourwebsite.com</p>
      <p class="contact-line"><b>web</b> : www.yourwebsite.com</p>
    </div>
    <p class="address">123, Abc Street<br>0000 City, Country</p>
  </section>

  <!-- Back 1 -->
  <section class="card card-back-logo" style="left:622px; top:74px;">
    <div class="brand" style="left:30px; top:66px;">
      <span class="brand-dot" style="width:96px; height:96px;"></span>
      <span class="brand-name" style="font-size:46px; margin-left:28px;">technicaprime</span>
    </div>
    <p class="cities" style="top:238px;">*Perth *Brisbane *Seoul *Hongkong</p>
  </section>

  <!-- Back 2 -->
  <section class="card card-back-watermark" style="left:54px; top:445px;">
    <svg class="art" width="525" height="300" viewBox="0 0 525 300" aria-hidden="true">
      <circle cx="270" cy="148" r="140" fill="var(--faint-mark)"/>
    </svg>
    <div class="brand" style="left:0; width:525px; top:120px; justify-content:center;">
      <span class="brand-name" style="font-size:58px;">technicaprime</span>
    </div>
    <p class="cities" style="top:255px;">*Perth *Brisbane *Seoul *Hongkong</p>
  </section>

  <!-- Back 3 -->
  <section class="card card-back-sectors" style="left:622px; top:445px;">
    <div class="brand" style="left:96px; top:22px;">
      <span class="brand-dot" style="width:62px; height:62px;"></span>
      <span class="brand-name" style="font-size:32px; margin-left:22px;">technicaprime</span>
    </div>
    <div class="photo-strip">
      <div class="photo reclaimer" role="img" aria-label="Photo of a mining stacker-reclaimer at an ore yard"></div>
      <div class="photo turbine" role="img" aria-label="Photo of wind turbine blades over the sea"></div>
      <div class="photo platform" role="img" aria-label="Aerial photo of an offshore oil and gas platform"></div>
      <div class="photo carrier" role="img" aria-label="Photo of an LNG carrier ship at sea"></div>
    </div>
    <p class="cities" style="top:255px;">*Perth *Brisbane *Seoul *Hongkong</p>
  </section>

</body>
</html>
```